Description of Adventure Certificate:
We require a certificate, that will be awarded to winners of competitions and offered to fundraising organisations for a $ value or type of event service we provide.
The certificate will be professionally printed on thick high-quality paper.
Design concept: Adventurous outer border, and exciting theme.
Title: Adventure Certificate (adventurous font)
Content: "Bringing the Thrill of Adventure to you"
Awarded To:..........................................
From:....................................................
Amount / Event: ...................................
Redemption Location:...........................
Expires:.................................................
Events listed near the base of certificate: Community events, Sports celebrations, Team building, School activities, Festivals, Vacation Care, EXPO's, Trade Shows.
Contact: M: 0418 627 349
E: info@tidalkite.com.au
Images: Tidal Kite Logo
Adventure Certificate image
Carabiner

```html
<!DOCTYPE html>
<html lang="en">
<head>
<meta charset="utf-8">
<title>Adventure Certificate – Tidal Kite</title>
<link rel="stylesheet" href="https://fonts.googleapis.com/css2?family=Almendra:wght@700&family=Italianno&display=swap">
<style>
  :root {
    --wall-orange: #e98a3a;
    --wall-red: #c2412c;
    --wall-deep: #a8311f;
    --paper: #ffffff;
    --ink: #111111;
    --brown: #7a5a4c;
    --rule: #8b6b5e;
    --logo-bg: #000000;
    --logo-text: #ffffff;
  }
  * { margin: 0; padding: 0; box-sizing: border-box; }
  html, body { width: 1200px; height: 848px; overflow: hidden; background: var(--paper); }
  .certificate {
    position: relative;
    width: 1200px;
    height: 848px;
    overflow: hidden;
    font-family: "Italianno", cursive;
    color: var(--ink);
  }
  .backdrop-photo {
    position: absolute; inset: 0;
    background: linear-gradient(90deg, var(--wall-orange) 0%, #e4803a 28%, var(--wall-red) 48%, var(--wall-deep) 100%);
  }
  .summit-art {
    position: absolute;
    left: 300px; top: 22px;
    width: 634px; height: 160px;
    background: linear-gradient(180deg, rgba(0,0,0,0) 0%, rgba(0,0,0,0.35) 100%);
  }
  .paper {
    position: absolute;
    left: 96px; top: 177px;
    width: 1010px; height: 627px;
    background: var(--paper);
  }
  .frame { position: absolute; inset: 0; pointer-events: none; }
  .title-ornament {
    position: absolute;
    left: 446px; width: 310px; height: 26px;
    background: rgba(122, 90, 76, 0.18);
    border-radius: 50%;
  }
  .title-ornament.top { top: 212px; }
  .title-ornament.bottom { top: 342px; }
  .title-rules { position: absolute; left: 184px; top: 250px; }
  .title {
    position: absolute;
    left: 0; width: 1200px; top: 256px;
    text-align: center;
    font-family: "Almendra", serif;
    font-weight: 700;
    font-size: 60px;
    letter-spacing: 1px;
    color: var(--brown);
  }
  .tagline {
    position: absolute;
    left: 0; width: 1200px; top: 386px;
    text-align: center;
    font-size: 50px;
    color: var(--ink);
  }
  .field { position: absolute; display: flex; align-items: flex-end; font-size: 24px; color: #333; }
  .field .label { width: 155px; }
  .field .colon { width: 8px; }
  .field .line { width: 323px; border-bottom: 1px solid var(--rule); height: 20px; }
  .field.awarded { left: 342px; top: 456px; }
  .field.from { left: 342px; top: 507px; }
  .field.amount { left: 342px; top: 559px; }
  .field.redemption { left: 198px; top: 618px; }
  .field.redemption .label { width: 170px; }
  .field.redemption .line { width: 323px; }
  .field.expires { left: 763px; top: 618px; }
  .field.expires .label { width: 68px; }
  .field.expires .line { width: 174px; }
  .events {
    position: absolute; left: 201px; top: 666px;
    width: 540px; font-size: 19px; line-height: 21px; color: #222;
  }
  .contact {
    position: absolute; left: 201px; top: 728px;
    font-size: 19px; line-height: 21px; color: #222;
  }
  .brand-mark {
    position: absolute; left: 820px; top: 655px;
    width: 185px; height: 110px;
    background: var(--logo-bg);
    display: flex; align-items: center; justify-content: center;
  }
  .brand-mark span {
    font-family: "Almendra", serif; font-weight: 700;
    font-size: 30px; color: var(--logo-text);
  }
</style>
</head>
<body>
<main class="certificate">
  <div class="backdrop-photo" role="img" aria-label="Photo of a climber gripping holds on an orange and red indoor climbing wall"></div>
  <div class="summit-art" role="img" aria-label="Black mountain range silhouette rising above the certificate"></div>

  <div class="paper"></div>

  <svg class="frame" width="1200" height="848" viewBox="0 0 1200 848" aria-hidden="true">
    <g fill="var(--ink)">
      <rect x="115" y="174" width="180" height="7" rx="3"/>
      <rect x="935" y="174" width="170" height="7" rx="3"/>
      <rect x="275" y="800" width="650" height="7" rx="3"/>
      <rect x="93" y="185" width="7" height="600" rx="3"/>
      <rect x="1102" y="185" width="7" height="600" rx="3"/>
      <rect x="115" y="800" width="60" height="7" rx="3"/>
      <rect x="1030" y="800" width="60" height="7" rx="3"/>
    </g>
  </svg>

  <div class="title-ornament top" role="img" aria-label="Decorative scroll flourish above the title"></div>
  <div class="title-ornament bottom" role="img" aria-label="Decorative scroll flourish below the title"></div>
  <svg class="title-rules" width="834" height="90" viewBox="0 0 834 90" aria-hidden="true">
    <g stroke="var(--rule)" stroke-width="2" fill="var(--rule)">
      <line x1="0" y1="7" x2="834" y2="7"/>
      <line x1="0" y1="82" x2="834" y2="82"/>
      <circle cx="4" cy="7" r="4"/><circle cx="830" cy="7" r="4"/>
      <circle cx="4" cy="82" r="4"/><circle cx="830" cy="82" r="4"/>
    </g>
  </svg>

  <h1 class="title">Adventure Certificate</h1>
  <p class="tagline">Bringing the Thrill of Adventure to you</p>

  <div class="field awarded"><span class="label">Awarded To</span><span class="colon">:</span><span class="line"></span></div>
  <div class="field from"><span class="label">From</span><span class="colon">:</span><span class="line"></span></div>
  <div class="field amount"><span class="label">Amount / Event</span><span class="colon">:</span><span class="line"></span></div>
  <div class="field redemption"><span class="label">Redemption Location:</span><span class="line"></span></div>
  <div class="field expires"><span class="label">Expires:</span><span class="line"></span></div>

  <p class="events">Events listed near the base of certificate: Community events, Sports celebrations, Team building, School activities, Festivals, Vacation Care, EXPO's, Trade Shows.</p>
  <p class="contact">Contact: M: 0418 627 349<br>E: info@tidalkite.com.au</p>

  <div class="brand-mark"><span>Tidal Kite</span></div>
</main>
</body>
</html>
```